Welbourne Dental, P.C. New stationary and business card for modern Dental Office

We need a new stationary/envelope/business card design using our newly designed logo. We are looking for an upscale look. Our new logo is used on our signage, using black as the background and white for the lettering. We would like the stationary to have black, white, possible greys or silver. We are looking for a letterhead, envelope, and business card design for three different employees, as well as a 4th card, same design, but just general with no employee name.

Project Deadline Extended
Reason: We began this project in the middle of our move into our new office. Things got pretty hectic and we just didn't have the time to go through designs. We now settled in and finally eliminated the designs that didn't work for us. We would like to extend the project another 5 days, and then finalize our decision. Most of the submissions showed business cards alone, with no stationary designs. Our original request was for stationary and business cards. Please keep this in mind.

Target Market(s)

Dental patients expecting high quality, cosmetic dentistry

Industry/Entity Type

Business

Contact Information for Business Card

Will need a design using our logo. All cards will be the same, other than that one card will have Office Managers name, One for the Doctor, Hygienist,
1. Office Manager - Marisol Dubrovka
2. Hygienist - Kayleigh Morrow
3. Gordon T. Welbourne, D.D.S.
4. One general one with no staff names

Font styles to use
Other font styles liked:
• see upload

Colors
000000
1b1b1b
757575
c9c9c9
e8e8e8
ffffff

Requirements
Must have
• -Logo
• -Phone number (718)555-0193
• -Address: 4352 63rd Ave
• Lower Level
• Brooklyn, NY 11290

```html
<!DOCTYPE html>
<html lang="en">
<head>
<meta charset="utf-8">
<title>Welbourne Dental, P.C. — Stationery</title>
<link href="https://fonts.googleapis.com/css2?family=Marcellus&display=swap" rel="stylesheet">
<style>
  :root {
    --black: #000000;
    --ink: #1b1b1b;
    --mid-grey: #757575;
    --silver: #c9c9c9;
    --pale: #e8e8e8;
    --white: #ffffff;
    --stage: #e6e6e6;
  }
  * { box-sizing: border-box; margin: 0; padding: 0; }
  html, body { width: 1200px; height: 957px; overflow: hidden; }
  body {
    background: var(--stage);
    font-family: "Marcellus", serif;
    color: var(--ink);
    position: relative;
  }
  .sheet {
    position: absolute;
    background: var(--white);
    box-shadow: 0 2px 10px rgba(0,0,0,0.12);
    overflow: hidden;
  }
  .logo {
    position: absolute;
    display: flex;
    align-items: center;
    gap: 10px;
    white-space: nowrap;
  }
  .logo-ring {
    border: 2px solid var(--mid-grey);
    border-radius: 50%;
    flex: none;
  }
  .logo-name { color: var(--mid-grey); }

  .band { position: absolute; left: 0; bottom: 0; width: 100%; }
  .band svg { display: block; width: 100%; height: 100%; }

  .contact {
    position: absolute;
    display: flex;
    gap: 8px;
    color: var(--ink);
    line-height: 1.35;
  }
  .contact svg { flex: none; margin-top: 2px; }

  /* Letterhead */
  .letterhead { left: 40px; top: 40px; width: 560px; height: 792px; }
  .letterhead .logo { right: 36px; top: 40px; }
  .letterhead .logo-name { font-size: 22px; }
  .letterhead .logo-ring { width: 40px; height: 40px; }
  .letterhead .addr { left: 40px; bottom: 92px; font-size: 13px; }
  .letterhead .phone { left: 300px; bottom: 92px; font-size: 13px; }
  .letterhead .band { height: 56px; }

  /* Business card front */
  .card { width: 336px; height: 192px; }
  .card-front { left: 640px; top: 40px; background: var(--black); }
  .card-front .logo { left: 50%; top: 50%; transform: translate(-50%, -50%); }
  .card-front .logo-name { color: var(--white); font-size: 22px; }
  .card-front .logo-ring { width: 38px; height: 38px; border-color: var(--silver); }

  /* Business card back */
  .card-back { left: 640px; top: 256px; }
  .card-back .logo { right: 20px; top: 20px; }
  .card-back .logo-name { font-size: 13px; }
  .card-back .logo-ring { width: 20px; height: 20px; border-width: 1.5px; }
  .person { position: absolute; left: 24px; top: 52px; }
  .person-name { font-size: 17px; color: var(--ink); }
  .person-role { font-size: 10px; color: var(--mid-grey); margin-top: 2px; }
  .card-back .addr { left: 24px; top: 100px; font-size: 9.5px; }
  .card-back .divider {
    position: absolute; left: 24px; right: 24px; top: 140px;
    height: 1px; background: var(--silver);
  }
  .card-back .phone { right: 24px; top: 148px; font-size: 10px; }
  .card-back .band { height: 18px; }

  /* Envelope */
  .envelope { left: 640px; top: 520px; width: 520px; height: 270px; }
  .envelope .logo { right: 24px; top: 30px; }
  .envelope .logo-name { font-size: 18px; }
  .envelope .logo-ring { width: 30px; height: 30px; }
  .envelope .addr { left: 28px; top: 30px; font-size: 12px; }
  .envelope .phone { left: 28px; top: 100px; font-size: 12px; }
  .envelope .band { height: 40px; }
</style>
</head>
<body>

<section class="sheet letterhead" aria-label="Letterhead">
  <div class="logo"><span class="logo-name">Welbourne Dental, P.C.</span><span class="logo-ring"></span></div>
  <div class="contact addr">
    <svg width="11" height="15" viewBox="0 0 11 15"><path d="M5.5 0C2.5 0 0 2.4 0 5.4 0 9.4 5.5 15 5.5 15S11 9.4 11 5.4C11 2.4 8.5 0 5.5 0Zm0 7.6a2.2 2.2 0 1 1 0-4.4 2.2 2.2 0 0 1 0 4.4Z" fill="#1b1b1b"/></svg>
    <span>4352 63rd Ave, Lower Level<br>Brooklyn<br>NY 11290</span>
  </div>
  <div class="contact phone">
    <svg width="12" height="14" viewBox="0 0 12 14"><path d="M3 0 5 3.5 3.6 5c.7 1.6 1.8 2.9 3.3 3.9L8.5 7.6 12 9.8 10.6 12.8C5 12.6 0.8 7.6 0.4 1.8Z" fill="#1b1b1b"/></svg>
    <span>(718) 555-0193</span>
  </div>
  <div class="band">
    <svg viewBox="0 0 560 56" preserveAspectRatio="none">
      <rect x="0" y="0" width="560" height="12" fill="#000"/>
      <path d="M330 12 H560 V56 H352 C352 32 346 16 330 12 Z" fill="#c9c9c9"/>
      <path d="M330 12 H560 V18 H340 Z" fill="#757575" opacity=".5"/>
    </svg>
  </div>
</section>

<section class="sheet card card-front" aria-label="Business card front">
  <div class="logo"><span class="logo-name">Welbourne Dental, P.C.</span><span class="logo-ring"></span></div>
</section>

<section class="sheet card card-back" aria-label="Business card back">
  <div class="logo"><span class="logo-name">Welbourne Dental, P.C.</span><span class="logo-ring"></span></div>
  <div class="person">
    <div class="person-name">Anders Whitcombe</div>
    <div class="person-role">Director</div>
  </div>
  <div class="contact addr">
    <svg width="8" height="11" viewBox="0 0 11 15"><path d="M5.5 0C2.5 0 0 2.4 0 5.4 0 9.4 5.5 15 5.5 15S11 9.4 11 5.4C11 2.4 8.5 0 5.5 0Zm0 7.6a2.2 2.2 0 1 1 0-4.4 2.2 2.2 0 0 1 0 4.4Z" fill="#1b1b1b"/></svg>
    <span>4352 63rd Ave, Lower Level<br>Brooklyn<br>NY 11290</span>
  </div>
  <div class="divider"></div>
  <div class="contact phone">
    <span>(718) 555-0193</span>
    <svg width="9" height="11" viewBox="0 0 12 14"><path d="M3 0 5 3.5 3.6 5c.7 1.6 1.8 2.9 3.3 3.9L8.5 7.6 12 9.8 10.6 12.8C5 12.6 0.8 7.6 0.4 1.8Z" fill="#1b1b1b"/></svg>
  </div>
  <div class="band">
    <svg viewBox="0 0 336 18" preserveAspectRatio="none">
      <path d="M210 0 H336 V18 H222 C222 8 218 2 210 0 Z" fill="#c9c9c9"/>
    </svg>
  </div>
</section>

<section class="sheet envelope" aria-label="Envelope">
  <div class="logo"><span class="logo-name">Welbourne Dental, P.C.</span><span class="logo-ring"></span></div>
  <div class="contact addr">
    <svg width="10" height="14" viewBox="0 0 11 15"><path d="M5.5 0C2.5 0 0 2.4 0 5.4 0 9.4 5.5 15 5.5 15S11 9.4 11 5.4C11 2.4 8.5 0 5.5 0Zm0 7.6a2.2 2.2 0 1 1 0-4.4 2.2 2.2 0 0 1 0 4.4Z" fill="#1b1b1b"/></svg>
    <span>4352 63rd Ave, Lower Level<br>Brooklyn<br>NY 11290</span>
  </div>
  <div class="contact phone" style="left:190px;top:62px;">
    <svg width="11" height="13" viewBox="0 0 12 14"><path d="M3 0 5 3.5 3.6 5c.7 1.6 1.8 2.9 3.3 3.9L8.5 7.6 12 9.8 10.6 12.8C5 12.6 0.8 7.6 0.4 1.8Z" fill="#1b1b1b"/></svg>
    <span>(718) 555-0193</span>
  </div>
  <div class="band">
    <svg viewBox="0 0 520 40" preserveAspectRatio="none">
      <rect x="0" y="0" width="520" height="9" fill="#000"/>
      <path d="M300 9 H520 V40 H318 C318 22 314 12 300 9 Z" fill="#c9c9c9"/>
    </svg>
  </div>
</section>

</body>
</html>
```